Postcard Design

SUNNY MEADOW NEST Learning Center

I would to advertise summer camp for my daycare. Affordable fun summer camp...Children can enjoy gardening, arts and crafts, field days, water days, math, reading and more...

Call us or come visit!!
Days: Monday-Friday
Time: 8:00-5:00
Ages: 5-12

Requirements
Nice to have
• children having fun

```html
<!DOCTYPE html>
<html lang="en">
<head>
<meta charset="utf-8">
<title>Sunny Meadow Nest – Summer Camp Postcard</title>
<link rel="stylesheet" href="https://fonts.googleapis.com/css2?family=Arimo:wght@700&family=Gochi+Hand&display=swap">
<style>
  :root {
    --page-bg: #f2efea;
    --paper: #ffffff;
    --teal: #0aa39d;
    --orange: #f39223;
    --green: #a9cf38;
    --yellow: #f3ea4a;
    --lettering-yellow: #f1ec55;
    --lettering-green: #9cc23a;
    --call-orange: #f07a2a;
  }
  * { margin: 0; padding: 0; box-sizing: border-box; }
  html, body {
    width: 1200px;
    height: 993px;
    overflow: hidden;
    background: var(--page-bg);
  }
  .postcard {
    position: absolute;
    left: 20px;
    top: 48px;
    width: 835px;
    height: 645px;
    transform: scale(1.3892);
    transform-origin: top left;
    background: var(--green);
    overflow: hidden;
  }
  .postcard__art {
    position: absolute;
    inset: 0;
    width: 835px;
    height: 645px;
  }
  .camp-lettering {
    position: absolute;
    left: 17px;
    top: 22px;
    width: 318px;
    height: 120px;
    border-radius: 24px;
    background: linear-gradient(160deg, var(--lettering-yellow) 0%, #e6e85a 55%, var(--lettering-green) 100%);
  }
  .brand {
    position: absolute;
    left: 350px;
    top: 30px;
    width: 480px;
    text-align: center;
    font-family: "Arimo", Arial, sans-serif;
    font-weight: 700;
  }
  .brand__name {
    color: var(--teal);
    font-size: 30px;
    letter-spacing: 0.5px;
    line-height: 36px;
  }
  .brand__sub {
    color: var(--orange);
    font-size: 28px;
    line-height: 34px;
  }
  .bubble {
    position: absolute;
    border-radius: 50%;
    border: 7px solid var(--paper);
    color: #fff;
    font-family: "Gochi Hand", cursive;
    text-align: center;
    display: flex;
    flex-direction: column;
    justify-content: center;
  }
  .bubble--offer {
    left: 477px;
    top: 129px;
    width: 330px;
    height: 330px;
    background: var(--orange);
    font-size: 20px;
    line-height: 29px;
    padding-bottom: 20px;
  }
  .bubble--hours {
    left: 337px;
    top: 381px;
    width: 248px;
    height: 248px;
    background: var(--teal);
    font-size: 30px;
    line-height: 40px;
    padding-bottom: 18px;
  }
  .call-to-action {
    position: absolute;
    left: 450px;
    top: 565px;
    font-family: "Gochi Hand", cursive;
    font-size: 38px;
    color: var(--call-orange);
    transform: rotate(-5deg);
    transform-origin: left center;
    white-space: nowrap;
  }
</style>
</head>
<body>
  <section class="postcard">
    <svg class="postcard__art" viewBox="0 0 835 645" xmlns="http://www.w3.org/2000/svg">
      <defs>
        <linearGradient id="photoTone" x1="0" y1="0" x2="1" y2="1">
          <stop offset="0" stop-color="#d9493a"/>
          <stop offset="0.3" stop-color="#e8b796"/>
          <stop offset="0.65" stop-color="#d9a982"/>
          <stop offset="1" stop-color="#8fbf3c"/>
        </linearGradient>
      </defs>
      <rect class="bg-green" x="0" y="0" width="835" height="645" fill="var(--green)"/>
      <rect class="photo-area" x="0" y="140" width="485" height="505" fill="url(#photoTone)" role="img" aria-label="Photo of happy children lying head to head in a circle on grass, reaching toward the camera"/>
      <path class="header-paper" d="M0 0 H835 V170 C760 150 660 122 560 130 C420 142 260 192 120 182 C70 178 30 172 0 178 Z" fill="var(--paper)"/>
      <path class="header-wave" d="M0 184 C30 178 70 184 120 188 C260 198 420 148 560 136 C660 128 760 156 835 176" fill="none" stroke="var(--teal)" stroke-width="8"/>
      <circle class="paint-splash" cx="655" cy="505" r="48" fill="var(--yellow)" role="img" aria-label="Yellow paint splash decoration"/>
    </svg>

    <div class="camp-lettering" role="img" aria-label="Hand-lettered Summer Camp title with a smiling sun"></div>

    <header class="brand">
      <h1 class="brand__name">SUNNY MEADOW NEST</h1>
      <p class="brand__sub">Learning Center</p>
    </header>

    <div class="bubble bubble--offer">
      <p>Are you<br>looking for an affordable,<br>fun summer camp?<br>Children can enjoy:<br>gardening, arts and crafts,<br>field days, water days,<br>math, reading and more..</p>
    </div>

    <div class="bubble bubble--hours">
      <p>Monday Friday<br>8:00-5:00<br>Ages: 5-12</p>
    </div>

    <p class="call-to-action">Call us or come visit!!!</p>
  </section>
</body>
</html>
```